Steady at Heart: Renew Your Team Through the 6 Habits of Balance

I'm looking for a design that is clean, like the book "Look Sideways" by Milo Brecken. The book is about the principles of organic farming so I am looking for a color scheme that fits that image.
https://www.pagelantern.example/Look-Sideways-Value-Seeing-Other-ebook/dp/Q47K520ZTR/ref=sr_1_3?crid=58XQ2PL07ZV4M&keywords=milo+brecken&qid=1638739111&s=books&sprefix=milo+%2Cstripbooks%2C371&sr=1-3

I don't want a dark color scheme. I prefer a white or cream book with a bold font.

This book is a good example of what I am looking for:

https://www.pagelantern.example/Lamp-Small-Notes-Painting-Days/dp/0912736458/ref=rtpb_2/731-5529043-4417082?pd_rd_w=mq8z3&pf_rd_p=21c9e047-385b-4f7d-a1c2-6e30b8d7f914&pf_rd_r=KP3T8QZ2207LM4NX1VA5&pd_rd_r=e63a1f20-7c4d-4a91-b5e8-09f2d1c7a6e3&pd_rd_wg=3kR2x&pd_rd_i=0912736458&psc=1

Target Market(s)

CEOs and business owners who want to increase the trust in their brands

Industry/Entity Type

Management and Leadership

Colors
00AB8E
00BBA5
67D7C9
C6EFE9
E9F9F6
59FF00
82FF00
B8FF75
E3FFCB
F4FFEA
FFF300
FFF600
FEFA6F
FFFEC7
FFFEE8
FFC000
F8CF3A
FAE287
FDF2CF
FEFAEE

Requirements
Must have
• Author's name is: Harold Vesterby
Nice to have
• I have indicated some books that I like. I would be good to have a simple image such as an apple core or the earth's core or some other image of "core" but not absolutely necessary.
Should not have
• I don't want it to have a dark cover or be too heavy

```html
<!DOCTYPE html>
<html lang="en">
<head>
<meta charset="utf-8">
<title>Steady at Heart — Book Cover</title>
<link rel="stylesheet" href="https://fonts.googleapis.com/css2?family=Jost:ital,wght@0,400;0,500;0,600;1,400&display=swap">
<style>
  :root {
    --paper: #ffffff;
    --ink: #161616;
    --green-deep: #12c44a;
    --green-bright: #59ff00;
    --apple-light: #b8ff75;
    --apple-mid: #7ed321;
    --apple-dark: #3f9a10;
  }
  * { box-sizing: border-box; margin: 0; padding: 0; }
  html, body {
    width: 1200px;
    height: 794px;
    overflow: hidden;
    background: var(--paper);
    font-family: "Jost", "Futura", sans-serif;
    color: var(--ink);
  }
  .canvas {
    width: 1200px;
    height: 794px;
    display: flex;
    justify-content: center;
  }
  .cover {
    width: 540px;
    height: 794px;
    background: var(--paper);
    display: flex;
    flex-direction: column;
    align-items: center;
    text-align: center;
  }
  .title { display: flex; flex-direction: column; align-items: center; margin-top: 44px; }
  .title-lead {
    font-weight: 600;
    font-size: 104px;
    line-height: 0.95;
    letter-spacing: -0.01em;
    background: linear-gradient(90deg, var(--green-deep), var(--green-bright) 55%, var(--green-deep));
    -webkit-background-clip: text;
    background-clip: text;
    color: transparent;
  }
  .title-link {
    font-weight: 500;
    font-size: 62px;
    line-height: 1.1;
    margin-top: 6px;
  }
  .title-main {
    font-weight: 500;
    font-size: 128px;
    line-height: 1;
    letter-spacing: -0.01em;
    margin-top: 4px;
  }
  .subtitle {
    font-size: 21px;
    line-height: 1.2;
    margin-top: 12px;
    font-weight: 400;
  }
  .subtitle em { font-style: italic; display: block; }
  .art-slot {
    width: 340px;
    height: 190px;
    margin-top: 20px;
    border-radius: 46% 46% 40% 40%;
    background: radial-gradient(ellipse at 40% 40%, var(--apple-light), var(--apple-mid) 55%, var(--apple-dark));
  }
  .author {
    margin-top: 36px;
    font-size: 30px;
    font-weight: 500;
    letter-spacing: 0.16em;
  }
</style>
</head>
<body>
  <main class="canvas">
    <article class="cover">
      <h1 class="title">
        <span class="title-lead">STEADY</span>
        <span class="title-link">AT</span>
        <span class="title-main">HEART</span>
      </h1>
      <p class="subtitle">Renew Your Team Through the <em>6 Habits of Balance</em></p>
      <div class="art-slot" role="img" aria-label="Photograph of a whole green apple beside a bitten green apple core"></div>
      <p class="author">AUTHOR NAME</p>
    </article>
  </main>
</body>
</html>
```